Flyer for Consulting Services (PM+Dev-Lead)

• The attached document describes consulting services for StartUps or young companies with a digital buisness model. We provide services for product management and development lead/scrum master. The target group of the flyer (i.e. who reads that flyer) is CEOs of Startups, Founders, Investors, Business Angle.s
• The task is to design an A4 flyer with one page layout (one pager) mostly for electronic destribution (printing second choice). There have to be two versions according given input: one in German and one in English with same layout. Preferably a format which allows us to adjust wording (e.g. Word, MS Publisher, …)
The final design should deliver professionality on one side and agility/StartUp mentality on the other side.

```html
<!DOCTYPE html>
<html lang="en">
<head>
<meta charset="utf-8">
<title>Product Management &amp; Development Consulting Flyer</title>
<link href="https://fonts.googleapis.com/css2?family=Bebas+Neue&family=Source+Sans+3:wght@400;600;700&display=swap" rel="stylesheet">
<style>
  :root {
    --blue: #1a9ad6;
    --blue-dark: #127bb0;
    --ink: #1f1f1f;
    --dark: #2e2e2e;
    --panel: #f2f2f2;
    --rule: #cfcfcf;
    --white: #ffffff;
    --muted: #3a3a3a;
  }
  * { box-sizing: border-box; margin: 0; padding: 0; }
  html, body { width: 946px; height: 1200px; overflow: hidden; background: #e9e9e9; }
  body { font-family: "Source Sans 3", "Myriad Pro", Arial, sans-serif; color: var(--ink); }

  .flyer { position: relative; width: 946px; height: 1200px; overflow: hidden; background: var(--panel); }

  /* Hero */
  .hero { position: absolute; left: 0; top: 0; width: 946px; height: 433px; }
  .hero-visual {
    position: absolute; inset: 0;
    background: radial-gradient(ellipse at 30% 55%, #d9d9d9 0%, #b9b9b9 45%, #8f8f8f 100%);
  }
  .hero-title {
    position: absolute; left: 0; right: 0; top: 26px;
    font-family: "Bebas Neue", Impact, sans-serif;
    font-size: 46px; line-height: 42px; letter-spacing: 1.5px;
    color: var(--white); text-align: center;
  }

  /* Left column */
  .audience { position: absolute; left: 0; top: 433px; width: 473px; height: 701px; background: var(--panel); }
  .audience-title {
    position: absolute; left: 30px; top: 34px;
    font-family: "Bebas Neue", Impact, sans-serif; font-size: 70px; line-height: 1; color: #111;
  }
  .need { position: absolute; left: 36px; display: flex; align-items: center; gap: 20px; }
  .need-icon { width: 80px; height: 84px; flex: none; }
  .need-text { font-size: 26px; line-height: 26px; color: var(--ink); }
  .need--idea { top: 116px; }
  .need--funding { top: 219px; }
  .need--support { top: 322px; }

  .contact { position: absolute; left: 20px; top: 441px; width: 418px; border-top: 2px solid var(--rule); }
  .contact-title { margin-top: 20px; font-weight: 700; font-size: 17px; letter-spacing: 1.5px; color: #111; }
  .person { margin-top: 16px; padding-left: 6px; font-size: 15px; line-height: 20.5px; color: var(--muted); }
  .person + .person { margin-top: 9px; }
  .person-line { display: flex; align-items: center; gap: 7px; }
  .person-line svg { width: 12px; height: 12px; flex: none; }

  .site-bar {
    position: absolute; left: 0; top: 1134px; width: 473px; height: 66px; background: var(--dark);
    display: flex; align-items: center; padding-left: 26px;
    color: var(--blue); font-size: 21px; font-weight: 600; letter-spacing: 2.2px;
  }

  /* Right column */
  .offer { position: absolute; left: 473px; top: 433px; width: 473px; height: 767px; background: var(--dark); }
  .offer-head {
    position: relative; height: 56px; background: var(--blue);
    color: var(--white); font-size: 27px; line-height: 56px; padding-left: 20px;
  }
  .offer-head::after {
    content: ""; position: absolute; left: 24px; bottom: -9px;
    border-left: 10px solid transparent; border-right: 10px solid transparent; border-top: 10px solid var(--blue);
  }
  .offer-list { list-style: none; padding: 22px 10px 0 20px; color: var(--white); font-size: 15px; line-height: 15.5px; }
  .offer-list li { display: flex; gap: 8px; margin-bottom: 10px; }
  .offer-list svg { width: 15px; height: 15px; flex: none; margin-top: 1px; }

  .offer-list--we { height: 186px; }
  .offer-list--wanted { height: 116px; padding-top: 24px; }
  .offer-list--benefits { height: 135px; }
  .offer-list--why { height: 107px; }
</style>
</head>
<body>
<main class="flyer">

  <section class="hero">
    <div class="hero-visual" role="img" aria-label="Photo of a businessman in glasses sketching a large light bulb on a grey wall, with many small hand-drawn bulbs around it"></div>
    <h1 class="hero-title">We are your partner for product management<br>and development!</h1>
  </section>

  <section class="audience">
    <h2 class="audience-title">You ...</h2>

    <div class="need need--idea">
      <svg class="need-icon" viewBox="0 0 80 84" aria-hidden="true">
        <ellipse cx="40" cy="80" rx="30" ry="3" fill="#c9c9c9"/>
        <circle cx="40" cy="40" r="38" fill="var(--blue)"/>
        <circle cx="40" cy="40" r="30" fill="var(--blue-dark)" opacity=".35"/>
        <circle cx="40" cy="34" r="12" fill="#fff"/>
        <rect x="34" y="44" width="12" height="9" fill="#fff"/>
        <rect x="35" y="55" width="10" height="3" rx="1.5" fill="#fff"/>
        <rect x="36" y="60" width="8" height="3" rx="1.5" fill="#fff"/>
      </svg>
      <p class="need-text">have a digital<br>business idea?</p>
    </div>

    <div class="need need--funding">
      <svg class="need-icon" viewBox="0 0 80 84" aria-hidden="true">
        <ellipse cx="40" cy="80" rx="30" ry="3" fill="#c9c9c9"/>
        <circle cx="40" cy="40" r="38" fill="var(--blue)"/>
        <circle cx="40" cy="40" r="30" fill="var(--blue-dark)" opacity=".35"/>
        <rect x="24" y="28" width="30" height="20" rx="3" fill="#fff" transform="rotate(-12 39 38)"/>
        <rect x="23" y="33" width="34" height="22" rx="3" fill="#fff"/>
        <rect x="23" y="38" width="34" height="5" fill="var(--blue)"/>
        <rect x="27" y="47" width="12" height="3" fill="var(--blue)"/>
      </svg>
      <p class="need-text">already obtained<br>a funding?</p>
    </div>

    <div class="need need--support">
      <svg class="need-icon" viewBox="0 0 80 84" aria-hidden="true">
        <ellipse cx="40" cy="80" rx="30" ry="3" fill="#c9c9c9"/>
        <circle cx="40" cy="40" r="38" fill="var(--blue)"/>
        <circle cx="40" cy="40" r="30" fill="var(--blue-dark)" opacity=".35"/>
        <circle cx="26" cy="32" r="5" fill="#fff"/>
        <circle cx="54" cy="32" r="5" fill="#fff"/>
        <path d="M17 50 q9 -13 18 0 z" fill="#fff"/>
        <path d="M45 50 q9 -13 18 0 z" fill="#fff"/>
        <circle cx="40" cy="36" r="6.5" fill="#fff"/>
        <path d="M28 57 q12 -18 24 0 z" fill="#fff"/>
      </svg>
      <p class="need-text">are looking for experienced<br>support for product<br>development?</p>
    </div>

    <div class="contact">
      <h3 class="contact-title">HOW TO CONTACT US?</h3>
      <div class="person">
        <p>Malte Kersting</p>
        <p>Agile Product Manager</p>
        <p class="person-line"><svg viewBox="0 0 12 12"><path d="M2 1 l2.5 0 l1 3 l-1.5 1 q1 2 3 3 l1 -1.5 l3 1 l0 2.5 q-1 1 -2.5 1 q-7 -2 -7.5 -7.5 q0 -1.5 1 -2.5z" fill="var(--blue)"/></svg>+49-170-00 12 34 56</p>
        <p class="person-line"><svg viewBox="0 0 12 12"><rect x="0.5" y="2" width="11" height="8" fill="var(--blue)"/><path d="M0.5 2 l5.5 4.5 l5.5 -4.5" fill="none" stroke="#fff" stroke-width="1"/></svg>contact@kersting-consult.de</p>
      </div>
      <div class="person">
        <p>Lars Brandt</p>
        <p>Scrum Master, Dev-Lead</p>
        <p class="person-line"><svg viewBox="0 0 12 12"><path d="M2 1 l2.5 0 l1 3 l-1.5 1 q1 2 3 3 l1 -1.5 l3 1 l0 2.5 q-1 1 -2.5 1 q-7 -2 -7.5 -7.5 q0 -1.5 1 -2.5z" fill="var(--blue)"/></svg>+49-171-0 98 76 54</p>
        <p class="person-line"><svg viewBox="0 0 12 12"><rect x="0.5" y="2" width="11" height="8" fill="var(--blue)"/><path d="M0.5 2 l5.5 4.5 l5.5 -4.5" fill="none" stroke="#fff" stroke-width="1"/></svg>lars.brandt@nordlabs.de</p>
      </div>
    </div>
  </section>

  <footer class="site-bar">www.kersting-consult.de</footer>

  <section class="offer">
    <svg width="0" height="0" style="position:absolute">
      <symbol id="tick" viewBox="0 0 15 15">
        <rect x="1" y="3" width="11" height="11" fill="none" stroke="var(--blue)" stroke-width="1.4"/>
        <path d="M4 8 l3 3 l7 -9" fill="none" stroke="var(--blue)" stroke-width="1.8"/>
      </symbol>
    </svg>

    <h2 class="offer-head">We …</h2>
    <ul class="offer-list offer-list--we">
      <li><svg><use href="#tick"/></svg><span>take over interim roles as: Product Owner, Scrum Master, and Dev-Lead</span></li>
      <li><svg><use href="#tick"/></svg><span>create your development team, optionally with offshore/nearshore locations</span></li>
      <li><svg><use href="#tick"/></svg><span>setup the cloud environment for your solution and support its operations</span></li>
      <li><svg><use href="#tick"/></svg><span>jointly establish an agile/lean mindset including corresponding procedures</span></li>
    </ul>

    <h2 class="offer-head">If wanted, …</h2>
    <ul class="offer-list offer-list--wanted">
      <li><svg><use href="#tick"/></svg><span>together we evolve your strategic orientation</span></li>
      <li><svg><use href="#tick"/></svg><span>support you in architecture and technology design</span></li>
      <li><svg><use href="#tick"/></svg><span>train you in product management and in creating a scalable agile organisation</span></li>
    </ul>

    <h2 class="offer-head">Your benefits...</h2>
    <ul class="offer-list offer-list--benefits">
      <li><svg><use href="#tick"/></svg><span>You focus on your ideas and your business model</span></li>
      <li><svg><use href="#tick"/></svg><span>You receive a professional realization of your ideas – in quality, time and budget</span></li>
      <li><svg><use href="#tick"/></svg><span>Our lean/agile mindset supports your start-up mentality and your commercial success</span></li>
    </ul>

    <h2 class="offer-head">Why us?</h2>
    <ul class="offer-list offer-list--why">
      <li><svg><use href="#tick"/></svg><span>Combined expertise in product management, development, and operations</span></li>
      <li><svg><use href="#tick"/></svg><span>Founders with experiences in digital business models and numerous industries</span></li>
    </ul>
  </section>

</main>
</body>
</html>
```